female esthetician looking for an impact business card

I an an expert in skin care industry with high experience in NYC.I want my business card to look professional , an impact at first look. I do want a combination between white and gold . I believe the font will be great if is gold.. The Fonts are also important. MIRELA COSTANDI (SKIN CARE BOUTIQUE)

THIS SHOULD BE THE BUSINESS NAME, and should be placed on th eback of the card.
IN front m, the name MIRELA COSTANDI - ESTHETCIAN

BY APPOINTMENTS ONLY: 512.478.2936

Target Market(s)

HIGH END CLIENTELE

Contact Information for Business Card

iT WILL BE on a luxury paper. I neeed the wow feeling

Requirements
Should not have
• pictures

```html
<!DOCTYPE html>
<html lang="en">
<head>
<meta charset="utf-8">
<title>Mirela Costandi – Business Card</title>
<link href="https://fonts.googleapis.com/css2?family=Cinzel:wght@400;600&display=swap" rel="stylesheet">
<style>
  :root {
    --backdrop: #dcdcdc;
    --paper: #efe9cb;
    --gold: #d6a66c;
    --gold-line: #e2c9a0;
  }
  * { margin: 0; padding: 0; box-sizing: border-box; }
  html, body {
    width: 1200px; height: 897px; overflow: hidden;
    background: var(--backdrop);
    font-family: "Cinzel", serif;
    color: var(--gold);
  }
  .canvas { position: relative; width: 1200px; height: 897px; }
  .card {
    position: absolute; left: 329px; width: 543px; height: 310px;
    background: var(--paper);
  }
  .card--front { top: 108px; }
  .card--back { top: 479px; }

  .front-header { position: absolute; right: 26px; top: 27px; text-align: right; }
  .holder-name { font-size: 22px; font-weight: 600; letter-spacing: 0.5px; line-height: 1; }
  .holder-title { font-size: 14px; font-weight: 400; letter-spacing: 0.6px; line-height: 1; margin-top: 8px; }
  .accent-bar {
    position: absolute; right: 0; top: 29px; width: 12px; height: 33px; background: var(--gold);
  }
  .divider {
    position: absolute; right: 24px; top: 77px; width: 184px; height: 1px; background: var(--gold-line);
  }
  .appointments {
    position: absolute; right: 24px; top: 92px; font-size: 13px; letter-spacing: 0.4px; line-height: 1;
  }

  .contact-list { position: absolute; left: 28px; top: 256px; list-style: none; }
  .contact-item { display: flex; align-items: center; font-size: 13.5px; line-height: 1; height: 20px; }
  .contact-icon { width: 9px; height: 9px; margin-right: 7px; fill: var(--gold); }

  .brand { position: absolute; left: 0; right: 0; top: 114px; text-align: center; }
  .brand-name { font-size: 39px; font-weight: 600; letter-spacing: 0.5px; line-height: 1; }
  .brand-tagline { font-size: 33px; font-weight: 400; letter-spacing: 0.5px; line-height: 1; margin-top: 14px; }
</style>
</head>
<body>
<main class="canvas">
  <section class="card card--front" aria-label="Card front">
    <header class="front-header">
      <h1 class="holder-name">MIRELA COSTANDI</h1>
      <p class="holder-title">ESTHETICIAN</p>
    </header>
    <div class="accent-bar"></div>
    <div class="divider"></div>
    <p class="appointments">BY APPOINTMENTS ONLY</p>
    <ul class="contact-list">
      <li class="contact-item">
        <svg class="contact-icon" viewBox="0 0 10 10" aria-hidden="true"><path d="M2 0.5 L3.6 0.5 L4.2 2.8 L3.1 3.6 Q4 5.8 6.2 7 L7.1 5.9 L9.5 6.5 L9.5 8.2 Q9.5 9.5 8 9.5 Q1 8.6 0.5 2 Q0.5 0.5 2 0.5 Z"/></svg>
        5124782936
      </li>
      <li class="contact-item">
        <svg class="contact-icon" viewBox="0 0 10 10" aria-hidden="true"><path d="M0.5 2 H9.5 V8 H0.5 Z M1.3 2.8 V7.2 H8.7 V2.8 L5 5.3 Z" fill-rule="evenodd"/></svg>
        MIRELACOSTANDI@MAILBOX.COM
      </li>
    </ul>
  </section>

  <section class="card card--back" aria-label="Card back">
    <div class="brand">
      <h2 class="brand-name">MIRELA COSTANDI</h2>
      <p class="brand-tagline">SKIN CARE BOUTIQUE</p>
    </div>
  </section>
</main>
</body>
</html>
```